Home care agency

Current website QRVCAREPLUS.com. Need to update and reformat to different pages. use my info from my current website

Target Market(s)

adult children

Industry/Entity Type

Home Health

Coding

Coded - Design and coding required

Number of Pages Required

4 page

Font styles to use
Sans Serif

Colors
3276b5
33a6d7
3277b5
85cae6
85acd3

```html
<!DOCTYPE html>
<html lang="en">
<head>
<meta charset="utf-8">
<title>QRV Care Plus – Home Health Care</title>
<link href="https://fonts.googleapis.com/css2?family=Nunito:wght@700;800;900&family=Poppins:wght@300;400;500;600&display=swap" rel="stylesheet">
<style>
:root{
  --blue:#3276b5;
  --sky:#33a6d7;
  --blue-2:#3277b5;
  --light:#85cae6;
  --soft:#85acd3;
  --ink:#2b2b2b;
  --grey:#7a7a7a;
  --white:#ffffff;
  --head:'Nunito',sans-serif;
  --body:'Poppins',sans-serif;
}
*{margin:0;padding:0;box-sizing:border-box}
html,body{width:1200px;height:3597px;overflow:hidden;background:var(--white)}
body{position:relative;font-family:var(--body);color:var(--ink)}
.abs{position:absolute}
.btn{position:absolute;background:var(--blue);color:var(--white);font:600 12px var(--body);display:flex;align-items:center;justify-content:center;gap:6px;border-radius:3px}
.btn svg{width:7px;height:9px}
.eyebrow{position:absolute;font:800 19px var(--head);color:var(--blue)}
.title{position:absolute;font:900 44px var(--head);color:var(--ink);letter-spacing:1px}
.copy{position:absolute;font:300 12px/20px var(--body);color:var(--grey)}

/* header */
.top-info{position:absolute;top:45px;font:400 12px/16px var(--body);color:var(--ink);display:flex;gap:8px;align-items:center}
.top-info small{display:block;font-size:11px;color:var(--grey)}
.brand{position:absolute;left:500px;top:40px;width:200px;text-align:center;font:800 22px var(--head);color:var(--blue)}
.nav{position:absolute;left:161px;top:116px;width:877px;height:43px;background:var(--blue);border-radius:4px;display:flex;justify-content:center;align-items:center;gap:28px;font:500 13px var(--body);color:var(--white)}
.nav .active{border-bottom:2px solid var(--white);padding:2px 6px}

/* hero */
.hero-photo{position:absolute;left:57px;top:138px;width:1086px;height:514px;background:linear-gradient(120deg,#8a7f72,#5a5048 45%,#3e3a36 75%,#6b625a)}
.hero-title{position:absolute;left:162px;top:326px;font:800 30px/38px var(--head);color:var(--white)}
.dots{position:absolute;display:flex;gap:8px;align-items:center}
.dots i{width:5px;height:5px;border-radius:50%;background:var(--white)}
.dots i.on{width:10px;height:10px;background:none;border:2px solid var(--white)}

/* stats */
.stat{position:absolute;width:300px;text-align:center}
.stat .num{font:900 46px/1 var(--head);color:var(--blue)}
.stat .lbl{font:700 17px var(--head);color:var(--ink);margin-top:6px}
.stat .desc{font:300 12px/20px var(--body);color:var(--grey);margin-top:8px}

/* services */
.services-band{position:absolute;left:0;top:1457px;width:1200px;height:576px}
.card{position:absolute;top:1704px;width:278px;height:210px;background:var(--white);border-radius:8px;text-align:center}
.card-photo{position:absolute;top:1609px;width:208px;height:162px;border:6px solid var(--white);border-radius:6px;box-shadow:0 2px 6px rgba(0,0,0,.12)}
.card h3{margin-top:86px;font:800 18px var(--head);color:var(--blue)}
.card p{font:300 11px/18px var(--body);color:var(--grey);padding:6px 30px 0}
.card .more{margin-top:8px;font:600 11px var(--body);color:var(--blue)}

/* nurses */
.nurse-photo{position:absolute;width:154px;height:106px;border:6px solid var(--sky);border-radius:12px}
.nurse-name{position:absolute;width:200px;text-align:center;font:800 18px var(--head);color:var(--blue)}
.nurse-role{position:absolute;width:200px;text-align:center;font:500 12px var(--body);color:var(--sky)}
.line-item{position:absolute;font:400 12px var(--body);color:var(--grey);display:flex;align-items:center;gap:6px}

/* testimonials */
.testimonial{position:absolute;left:161px;top:2494px;width:877px;height:299px;border-radius:16px;background:linear-gradient(100deg,var(--light),var(--sky) 50%,#5c9cc7);text-align:center;color:var(--white)}

/* contact */
.field{position:absolute;left:235px;width:301px;height:30px;border-bottom:1px solid #cfcfcf;display:flex;align-items:center;gap:10px;font:italic 300 12px var(--body);color:var(--grey);padding-left:2px}
.field svg{width:12px;height:12px}

/* footer */
.footer-photo{position:absolute;left:49px;top:3272px;width:1103px;height:278px;background:linear-gradient(90deg,#5b3c22,#8a5526 40%,#a8641f 70%,#6e4a2c)}
.foot-col{position:absolute;top:3326px;color:var(--white)}
.foot-col h4{font:800 18px var(--head);margin-bottom:16px}
.foot-col li{list-style:none;font:400 12px/30px var(--body);display:flex;align-items:center;gap:8px}
.copyright{position:absolute;left:0;top:3550px;width:1200px;height:47px;background:var(--blue);color:var(--white);font:400 12px var(--body);display:flex;align-items:center;justify-content:center}
</style>
</head>
<body>

<!-- header -->
<header>
  <div class="top-info" style="left:162px">
    <svg width="24" height="22" viewBox="0 0 24 22"><path d="M12 1 1 11h3v10h6v-6h4v6h6V11h3z" fill="var(--blue)"/></svg>
    <div><small>Location</small>PO Box 48 Bayview, MA 02190</div>
  </div>
  <div class="brand">QRV Care Plus</div>
  <div class="top-info" style="left:908px">
    <svg width="22" height="22" viewBox="0 0 24 24"><path d="M6.6 10.8a15 15 0 0 0 6.6 6.6l2.2-2.2a1 1 0 0 1 1-.25 11 11 0 0 0 3.6.6 1 1 0 0 1 1 1V20a1 1 0 0 1-1 1A17 17 0 0 1 3 4a1 1 0 0 1 1-1h3.5a1 1 0 0 1 1 1c0 1.25.2 2.45.6 3.6a1 1 0 0 1-.25 1z" fill="var(--blue)"/></svg>
    <div style="text-align:right"><small>Service Available</small>555-014-2290</div>
  </div>
</header>

<!-- hero -->
<section class="hero">
  <div class="abs" style="left:0;top:224px;width:57px;height:342px;background:var(--sky)"></div>
  <div class="abs" style="left:1143px;top:182px;width:57px;height:526px;background:var(--blue)"></div>
  <div class="abs" style="left:562px;top:652px;width:638px;height:56px;background:var(--blue)"></div>
  <div class="hero-photo" role="img" aria-label="Nurse caring for an elderly man at home"></div>
  <nav class="nav">
    <span class="active">Home</span><span>About</span><span>Services</span><span>Nurses</span><span>Contact</span>
    <svg width="13" height="13" viewBox="0 0 14 14"><circle cx="6" cy="6" r="4.5" stroke="#fff" stroke-width="2" fill="none"/><path d="m9.5 9.5 3.5 3.5" stroke="#fff" stroke-width="2"/></svg>
  </nav>
  <h1 class="hero-title">Providing Care Throughout<br>the South Shore</h1>
  <div class="btn" style="left:162px;top:422px;width:126px;height:35px">Contact <svg viewBox="0 0 7 9"><path d="m1 1 4 3.5L1 8" stroke="#fff" stroke-width="1.6" fill="none"/></svg></div>
  <div class="dots" style="left:583px;top:615px"><i></i><i></i><i class="on"></i></div>
</section>

<!-- about -->
<section class="about">
  <div class="abs" style="left:161px;top:752px;width:427px;height:363px;background:linear-gradient(135deg,#a9a097,#e8e0d4 50%,#8f8478)" role="img" aria-label="Portrait of founder Dana Whitfield, registered nurse"></div>
  <div class="eyebrow" style="left:612px;top:777px">Introduction</div>
  <h2 class="title" style="left:612px;top:806px">ABOUT</h2>
  <p class="copy" style="left:612px;top:867px;width:370px">QRV Care Plus Home Health Services is owned and operated by Dana Whitfield. Dana is a registered nurse and has been in the health care system since 2001. She has specialized in home care, cardiology, trauma and critical care.</p>
  <p class="copy" style="left:612px;top:968px;width:370px">She invests in future caregivers and has taught for the nursing programs at Harborline University, Coastal Health Institute, and Westmere College.</p>
  <div class="btn" style="left:612px;top:1049px;width:127px;height:36px">Read More <svg viewBox="0 0 7 9"><path d="m1 1 4 3.5L1 8" stroke="#fff" stroke-width="1.6" fill="none"/></svg></div>
</section>

<!-- stats -->
<section class="stats">
  <svg class="abs" style="left:270px;top:1170px" width="60" height="110" viewBox="0 0 60 110">
    <path d="M30 38 12 20a9 9 0 0 1 18-9 9 9 0 0 1 18 9z" fill="none" stroke="var(--blue)" stroke-width="1.6"/>
    <path d="M8 22h12l4-7 5 12 4-8h19" fill="none" stroke="var(--blue)" stroke-width="1.6"/>
    <path d="M30 44c-12 18 12 30 0 62" fill="none" stroke="var(--sky)" stroke-dasharray="3 3"/>
  </svg>
  <svg class="abs" style="left:570px;top:1170px" width="60" height="110" viewBox="0 0 60 110">
    <circle cx="30" cy="19" r="17" fill="none" stroke="var(--blue)" stroke-width="1.6"/>
    <circle cx="24" cy="15" r="1.6" fill="var(--blue)"/><circle cx="36" cy="15" r="1.6" fill="var(--blue)"/>
    <path d="M22 23q8 8 16 0" fill="none" stroke="var(--blue)" stroke-width="1.6"/>
    <path d="M30 40c-12 18 12 30 0 66" fill="none" stroke="var(--sky)" stroke-dasharray="3 3"/>
  </svg>
  <svg class="abs" style="left:870px;top:1170px" width="60" height="110" viewBox="0 0 60 110">
    <rect x="12" y="6" width="36" height="30" rx="3" fill="none" stroke="var(--blue)" stroke-width="1.6"/>
    <path d="M12 14h36M20 2v8M40 2v8" stroke="var(--blue)" stroke-width="1.6"/>
    <circle cx="30" cy="25" r="6" fill="none" stroke="var(--blue)" stroke-width="1.4"/>
    <path d="m27 25 2 2 4-4" fill="none" stroke="var(--blue)" stroke-width="1.4"/>
    <path d="M30 40c-12 18 12 30 0 66" fill="none" stroke="var(--sky)" stroke-dasharray="3 3"/>
  </svg>
  <div class="stat" style="left:150px;top:1286px"><div class="num">625+</div><div class="lbl">Case Studies</div><div class="desc">Bring best quality health services<br>to ones who are in need</div></div>
  <div class="stat" style="left:450px;top:1286px"><div class="num">1000+</div><div class="lbl">Happy Clients</div><div class="desc">Our hospitals are equipped with<br>the latest utilities, technologies,</div></div>
  <div class="stat" style="left:750px;top:1286px"><div class="num">1500+</div><div class="lbl">project done</div><div class="desc">Bring best We established<br>cooperation with plenty of globally</div></div>
</section>

<!-- services -->
<section class="services">
  <svg class="services-band" viewBox="0 0 1200 576" preserveAspectRatio="none"><path d="M0 0h1200v527Q600 610 0 527z" fill="var(--sky)"/></svg>
  <div class="eyebrow" style="left:0;width:1200px;text-align:center;top:1498px;color:var(--white)">Why Choose Home Care?</div>
  <h2 class="title" style="left:0;width:1200px;text-align:center;top:1525px;color:var(--white)">SERVICES</h2>

  <div class="card" style="left:161px"><h3>Medication Management</h3><p>Lorem Ipsum has been the industry's standard dummy text ever since the 1500s,</p><div class="more">Read More ›</div></div>
  <div class="card" style="left:461px"><h3>Meal Preparations</h3><p>Lorem Ipsum has been the industry's standard dummy text ever since the 1500s,</p><div class="more">Read More ›</div></div>
  <div class="card" style="left:761px"><h3>Wound Care</h3><p>Lorem ipsum has been the industry's standard dummy text ever since the 1500s,</p><div class="more">Read More ›</div></div>
  <div class="card-photo" style="left:196px;background:linear-gradient(135deg,#d9c7b3,#eee7dd 50%,#9aa38a)" role="img" aria-label="Caregiver helping a senior woman with medication"></div>
  <div class="card-photo" style="left:496px;background:linear-gradient(135deg,#c8ccd2,#ece9e4 50%,#b9ab98)" role="img" aria-label="Caregiver serving a meal to an elderly man"></div>
  <div class="card-photo" style="left:796px;background:linear-gradient(135deg,#bcd7ea,#f2f4f6 55%,#d9c2b0)" role="img" aria-label="Hands applying a wound bandage"></div>

  <div class="abs" style="left:536px;top:1946px;width:128px;height:36px;background:var(--white);border-radius:3px;font:600 12px var(--body);color:var(--blue);display:flex;align-items:center;justify-content:center">View All ›</div>
</section>

<!-- nurses -->
<section class="nurses">
  <div class="nurse-photo" style="left:190px;top:2096px;background:linear-gradient(135deg,#8e8276,#e7ddd0)" role="img" aria-label="Photo of nurse Dana Whitfield"></div>
  <div class="nurse-photo" style="left:415px;top:2096px;background:linear-gradient(135deg,#d8d8d8,#f4f4f4)" role="img" aria-label="Photo of nurse Julia Smith"></div>
  <div class="nurse-photo" style="left:190px;top:2298px;background:linear-gradient(135deg,#a9c6d6,#e6eef2)" role="img" aria-label="Photo of nurse Julia Smith"></div>
  <div class="nurse-photo" style="left:415px;top:2298px;background:linear-gradient(135deg,#9fbcd3,#eef2f5)" role="img" aria-label="Photo of nurse Julia Smith"></div>
  <div class="nurse-name" style="left:164px;top:2214px">Dana Whitfield</div><div class="nurse-role" style="left:164px;top:2245px">Nurse</div>
  <div class="nurse-name" style="left:389px;top:2214px">Julia Smith</div><div class="nurse-role" style="left:389px;top:2245px">Nurse</div>
  <div class="nurse-name" style="left:164px;top:2417px">Julia Smith</div><div class="nurse-role" style="left:164px;top:2448px">Nurse</div>
  <div class="nurse-name" style="left:389px;top:2417px">Julia Smith</div><div class="nurse-role" style="left:389px;top:2448px">Nurse</div>

  <div class="eyebrow" style="left:610px;top:2139px">Meet Nurses</div>
  <h2 class="title" style="left:610px;top:2168px">CARE GIVER</h2>
  <p class="copy" style="left:610px;top:2231px;width:320px;font-size:11px;line-height:18px">Lorem ipsum has been the industry's standard dummy text ever since the 1500s, Lorem Ipsum has been the industry's standard dummy text ever since the 1500s,</p>
  <div class="line-item" style="left:610px;top:2305px">
    <svg width="11" height="11" viewBox="0 0 24 24"><path d="M6.6 10.8a15 15 0 0 0 6.6 6.6l2.2-2.2a1 1 0 0 1 1-.25 11 11 0 0 0 3.6.6 1 1 0 0 1 1 1V20a1 1 0 0 1-1 1A17 17 0 0 1 3 4a1 1 0 0 1 1-1h3.5a1 1 0 0 1 1 1c0 1.25.2 2.45.6 3.6a1 1 0 0 1-.25 1z" fill="var(--blue)"/></svg>555-014-2290
    <svg style="margin-left:12px" width="12" height="10" viewBox="0 0 12 10"><rect width="12" height="10" rx="1" fill="var(--blue)"/><path d="m1 1 5 4 5-4" stroke="#fff" fill="none"/></svg>info@example.com
  </div>
  <div class="line-item" style="left:610px;top:2339px">
    <svg width="9" height="12" viewBox="0 0 9 12"><path d="M4.5 0A4.5 4.5 0 0 0 0 4.5C0 8 4.5 12 4.5 12S9 8 9 4.5A4.5 4.5 0 0 0 4.5 0z" fill="var(--blue)"/><circle cx="4.5" cy="4.5" r="1.6" fill="#fff"/></svg>PO Box 48 Bayview, MA 02190
  </div>
  <div class="abs" style="left:610px;top:2396px;width:249px;height:30px;border-bottom:2px solid var(--blue);font:italic 300 11px var(--body);color:#aaa;padding-top:4px">Your Email Address*</div>
  <div class="btn" style="left:872px;top:2390px;width:127px;height:37px">Subscribe <svg viewBox="0 0 7 9"><path d="m1 1 4 3.5L1 8" stroke="#fff" stroke-width="1.6" fill="none"/></svg></div>
</section>

<!-- testimonials -->
<section class="testimonial" role="img" aria-label="Soft blue background image of a caregiver with a client">
  <div style="margin-top:26px;font:800 19px var(--head)">Client Reviews</div>
  <div style="margin-top:2px;font:900 44px var(--head);letter-spacing:1px">TESTIMONIALS</div>
  <p style="margin:10px auto 0;width:440px;font:300 12px/18px var(--body)">Lorem ipsum has been the industry's standard dummy text ever since the 1500s, Lorem ipsum has been the industry's standard dummy text ever since the 1500s,</p>
  <div style="margin-top:8px;font:800 18px var(--head)">Julia Smith</div>
  <div style="margin-top:2px;font:500 13px var(--body)">Client</div>
  <div class="dots" style="left:422px;top:260px"><i></i><i></i><i class="on"></i></div>
</section>

<!-- contact -->
<section class="contact">
  <div class="eyebrow" style="left:235px;top:2850px">Have Any Question?</div>
  <h2 class="title" style="left:235px;top:2878px">CONTACT</h2>
  <div class="field" style="top:2937px"><svg viewBox="0 0 12 12"><circle cx="6" cy="4" r="2.6" fill="none" stroke="var(--blue)"/><path d="M1.5 11.5a4.5 4.5 0 0 1 9 0" fill="none" stroke="var(--blue)"/></svg>Your Name*</div>
  <div class="field" style="top:2982px"><svg viewBox="0 0 12 12"><rect x="1" y="2.5" width="10" height="7" fill="none" stroke="var(--blue)"/><path d="m1 2.5 5 4 5-4" fill="none" stroke="var(--blue)"/></svg>Your Email*</div>
  <div class="field" style="top:3026px"><svg viewBox="0 0 24 24"><path d="M6.6 10.8a15 15 0 0 0 6.6 6.6l2.2-2.2a1 1 0 0 1 1-.25 11 11 0 0 0 3.6.6 1 1 0 0 1 1 1V20a1 1 0 0 1-1 1A17 17 0 0 1 3 4a1 1 0 0 1 1-1h3.5a1 1 0 0 1 1 1c0 1.25.2 2.45.6 3.6a1 1 0 0 1-.25 1z" fill="none" stroke="var(--blue)" stroke-width="2"/></svg>Your Phone*</div>
  <div class="field" style="top:3069px"><svg viewBox="0 0 12 12"><path d="M2.5 1h5l2 2v8h-7z" fill="none" stroke="var(--blue)"/><path d="M4 6h4M4 8h4" stroke="var(--blue)"/></svg>Your Subject*</div>
  <div class="btn" style="left:408px;top:3127px;width:128px;height:37px">Submit <svg viewBox="0 0 7 9"><path d="m1 1 4 3.5L1 8" stroke="#fff" stroke-width="1.6" fill="none"/></svg></div>
  <div class="abs" style="left:642px;top:2829px;width:364px;height:364px;border-radius:50%;background:linear-gradient(135deg,#8f8478,#e9e1d5 50%,#a79e93)" role="img" aria-label="Portrait of nurse Dana Whitfield"></div>
</section>

<!-- footer -->
<footer>
  <div class="abs" style="left:894px;top:3241px;width:306px;height:40px;background:var(--sky)"></div>
  <div class="abs" style="left:0;top:3336px;width:49px;height:166px;background:var(--blue)"></div>
  <div class="footer-photo" role="img" aria-label="Warm sunset scene of a person with open arms"></div>
  <div class="abs" style="left:162px;top:3382px;width:126px;text-align:center;font:800 18px var(--head);color:var(--white)">QRV Care Plus</div>
  <div class="abs" style="left:163px;top:3478px;display:flex;gap:7px">
    <i style="width:20px;height:20px;border-radius:50%;background:var(--white)"></i>
    <i style="width:20px;height:20px;border-radius:50%;background:var(--white)"></i>
    <i style="width:20px;height:20px;border-radius:50%;background:var(--white)"></i>
    <i style="width:20px;height:20px;border-radius:50%;background:var(--white)"></i>
  </div>
  <div class="foot-col" style="left:386px"><h4>Useful links</h4><ul><li>Blogs</li><li>Term &amp; Condition</li><li>Privacy policy</li><li>FAQ's</li><li>Location</li></ul></div>
  <div class="foot-col" style="left:611px"><h4>Quick links</h4><ul><li>Home</li><li>About</li><li>Services</li><li>Blogs</li></ul></div>
  <div class="foot-col" style="left:836px"><h4>Contact Us</h4><ul>
    <li><svg width="10" height="10" viewBox="0 0 24 24"><path d="M6.6 10.8a15 15 0 0 0 6.6 6.6l2.2-2.2a1 1 0 0 1 1-.25 11 11 0 0 0 3.6.6 1 1 0 0 1 1 1V20a1 1 0 0 1-1 1A17 17 0 0 1 3 4a1 1 0 0 1 1-1h3.5a1 1 0 0 1 1 1c0 1.25.2 2.45.6 3.6a1 1 0 0 1-.25 1z" fill="#fff"/></svg>(1) 123-456-7890</li>
    <li><svg width="11" height="9" viewBox="0 0 12 10"><rect width="12" height="10" rx="1" fill="#fff"/><path d="m1 1 5 4 5-4" stroke="#8a5526" fill="none"/></svg>info@example.com</li>
    <li><svg width="8" height="11" viewBox="0 0 9 12"><path d="M4.5 0A4.5 4.5 0 0 0 0 4.5C0 8 4.5 12 4.5 12S9 8 9 4.5A4.5 4.5 0 0 0 4.5 0z" fill="#fff"/></svg>12 Linden Court</li>
    <li>Ridgeview FL 30412</li>
  </ul></div>
  <div class="copyright">© 2019 QRV Care Plus | All Rights Reserved.</div>
</footer>

</body>
</html>
```